Updated look for company collateral

We are a staffing company specializing in placing accounting, finance and IT professionals in their next career. We are going through a rebrand as well, i have included several other pieces so you can see our vision for the future. We are looking for a front and back one pager. We have four divisions Our company needs an updated look for our company collateral - there are four versions of the content (Enterprise, IT, Healthcare IT and Accounting & Finance) the design will be the same (different images for each flyer but same template) I am looking for a template that could be updated for each division. I am including the content for the IT version.

Our design aesthetic is clean, well organized, but with interesting design elements. We want to be perceived as on trend, leader in our industry. We have been in business for almost 20 years and know our industry well and successfully, our workforce is youthful, energetic and competitive so we still want to have an element of fun and creativity in our collateral.

Font styles to use
Sans Serif

Requirements
Must have
• similar color themes as attached examples

```html
<!DOCTYPE html>
<html lang="en">
<head>
<meta charset="utf-8">
<title>Vantora Group – Flyer Front and Back</title>
<link rel="stylesheet" href="https://fonts.googleapis.com/css2?family=Montserrat:wght@400;500;600;700;800&family=Open+Sans:wght@400;600;700&display=swap">
<style>
  :root {
    --orange: #f18a1c;
    --orange-deep: #e8700a;
    --ink: #2b2f36;
    --bar: #1c1c1e;
    --paper: #ffffff;
    --backdrop: #d7d7d7;
    --body: #2e2e2e;
  }
  * { margin: 0; padding: 0; box-sizing: border-box; }
  html, body { width: 900px; height: 1200px; overflow: hidden; }
  body {
    background: var(--backdrop);
    font-family: "Open Sans", Arial, sans-serif;
    color: var(--body);
    position: relative;
  }
  .sheet {
    position: absolute;
    top: 296px;
    width: 430px;
    height: 607px;
    background: var(--paper);
    overflow: hidden;
    box-shadow: 0 2px 10px rgba(0,0,0,0.12);
  }
  .sheet--front { left: 16px; }
  .sheet--back { left: 454px; }
  .abs { position: absolute; }
  .deco { position: absolute; left: 0; top: 0; width: 430px; height: 607px; }

  /* Brand */
  .brand-mark {
    width: 27px; height: 27px; border-radius: 50%;
    background: var(--orange);
    left: 70px; top: 22px;
  }
  .brand-name {
    left: 20px; top: 57px;
    font-family: "Montserrat", sans-serif;
    font-weight: 600; font-size: 13px; letter-spacing: 1.5px;
    color: var(--ink); white-space: nowrap;
  }

  /* Photo placeholders */
  .photo-hero {
    left: 174px; top: 8px; width: 280px; height: 280px; border-radius: 50%;
    background: radial-gradient(circle at 45% 40%, #f4f2ee 0%, #d9d4cc 45%, #6f7687 75%, #2f3a58 100%);
  }
  .photo-office {
    left: -62px; top: 386px; width: 248px; height: 248px; border-radius: 50%;
    background: radial-gradient(circle at 40% 35%, #f1f0ec 0%, #cfc9bf 45%, #8b7560 75%, #4b3c30 100%);
  }
  .photo-desk {
    left: 0; top: 484px; width: 430px; height: 96px;
    background: linear-gradient(100deg, #3a3a3c 0%, #77736c 30%, #c8c4bc 55%, #8e8a84 75%, #4a4642 100%);
  }

  /* Headline */
  .headline { left: 21px; top: 126px; font-family: "Montserrat", sans-serif; white-space: nowrap; }
  .headline__dark { font-weight: 700; font-size: 13.2px; line-height: 17.5px; color: var(--ink); }
  .headline__accent { font-weight: 700; font-size: 14.4px; line-height: 21px; color: var(--orange); }
  .services-title {
    left: 21px; top: 215px;
    font-family: "Montserrat", sans-serif; font-weight: 400;
    font-size: 16px; line-height: 22px; color: var(--orange); letter-spacing: 0.3px;
  }
  .services-intro {
    left: 21px; top: 262px; width: 170px;
    font-size: 5.6px; line-height: 7.6px; color: var(--body);
  }

  /* Service list */
  .service-icon {
    width: 48px; height: 48px; border-radius: 50%;
    background: var(--paper); border: 3px solid var(--orange);
    display: flex; align-items: center; justify-content: center;
  }
  .service-icon__art { width: 28px; height: 28px; border-radius: 50%; }
  .service-icon--tech { left: 75px; top: 357px; }
  .service-icon--tech .service-icon__art { background: radial-gradient(circle, #ffd35a, #3fa9e0); }
  .service-icon--finance { left: 144px; top: 429px; }
  .service-icon--finance .service-icon__art { background: radial-gradient(circle, #f7a23c, #3b4f9a); }
  .service-icon--health { left: 159px; top: 517px; }
  .service-icon--health .service-icon__art { background: radial-gradient(circle, #c6b4f1, #5c6fcf); }

  .service__title {
    font-family: "Montserrat", sans-serif; font-weight: 600;
    font-size: 12.6px; line-height: 16px; color: var(--orange);
    white-space: nowrap;
  }
  .service__text { font-size: 6.9px; line-height: 9.4px; color: var(--body); margin-top: 2px; }
  .service--tech { left: 130px; top: 349px; width: 280px; }
  .service--tech .service__text { margin-left: 9px; width: 267px; }
  .service--finance { left: 199px; top: 425px; width: 214px; }
  .service--finance .service__text { margin-left: 10px; width: 203px; }
  .service--health { left: 207px; top: 506px; width: 205px; }
  .service--health .service__text { margin-left: 9px; width: 190px; }

  /* Footer bars */
  .contact-bar {
    background: var(--bar); color: #fff;
    display: flex; align-items: center;
    font-size: 9.6px; white-space: nowrap;
  }
  .contact-bar--front {
    left: 186px; top: 581px; width: 244px; height: 26px;
    border-radius: 12px 0 0 0; padding-left: 16px; gap: 12px;
  }
  .contact-bar--back {
    left: 0; top: 580px; width: 430px; height: 27px;
    padding: 0 12px; gap: 12px; font-size: 9.2px;
  }
  .contact-bar__item { display: flex; align-items: center; gap: 5px; }
  .contact-bar__icon { width: 9px; height: 9px; flex: none; }
  .contact-bar__address { font-size: 6.2px; line-height: 7.6px; }

  /* Back page */
  .about-title {
    right: 20px; top: 20px;
    font-family: "Montserrat", sans-serif; font-weight: 800;
    font-size: 18px; color: var(--orange); letter-spacing: 0.4px;
  }
  .about-rule { right: 20px; top: 44px; width: 56px; height: 2px; background: var(--ink); }
  .about-text { right: 19px; text-align: right; color: var(--body); white-space: nowrap; }
  .about-text--lead { top: 62px; font-size: 7.5px; line-height: 10.4px; }
  .about-text--detail { top: 167px; font-size: 6.8px; line-height: 9.5px; }

  .mission-title {
    left: 22px; top: 280px;
    font-family: "Montserrat", sans-serif; font-weight: 700;
    font-size: 10.4px; color: var(--orange); letter-spacing: 0.2px;
  }
  .mission-rule { left: 22px; top: 294px; width: 122px; height: 1.5px; background: var(--ink); }
  .mission-text { left: 22px; top: 302px; width: 388px; font-size: 7px; line-height: 9.6px; }

  .pledge { left: 22px; width: 392px; }
  .pledge__head {
    display: flex; align-items: center; gap: 4px;
    font-family: "Montserrat", sans-serif; font-weight: 700;
    font-size: 7.6px; color: var(--orange);
  }
  .pledge__chevron { width: 8px; height: 9px; flex: none; }
  .pledge__text { margin: 2px 0 0 13px; font-size: 6.3px; line-height: 8.6px; color: var(--body); }
  .pledge--customers { top: 343px; }
  .pledge--consultants { top: 388px; }
  .pledge--employees { top: 440px; }
</style>
</head>
<body>

<!-- FRONT -->
<section class="sheet sheet--front" aria-label="Flyer front">
  <div class="abs photo-hero" role="img" aria-label="Photo of a cheering office team raising their arms in celebration"></div>
  <div class="abs photo-office" role="img" aria-label="Photo of a bright open-plan office with people working at desks"></div>

  <svg class="deco" viewBox="0 0 430 607" aria-hidden="true">
    <defs>
      <linearGradient id="swoosh" x1="0" y1="0" x2="1" y2="0">
        <stop offset="0" stop-color="#f18a1c"/>
        <stop offset="0.55" stop-color="#e8700a"/>
        <stop offset="1" stop-color="#3a2a1c"/>
      </linearGradient>
    </defs>
    <circle cx="314" cy="148" r="144" fill="none" stroke="#f18a1c" stroke-width="5"/>
    <path d="M196 250 Q250 298 430 292" fill="none" stroke="#f18a1c" stroke-width="1.6"/>
    <circle cx="193" cy="246" r="4.5" fill="#fff" stroke="#f18a1c" stroke-width="1.6"/>
    <path d="M210 272 Q285 330 430 318" fill="none" stroke="url(#swoosh)" stroke-width="6" stroke-linecap="round"/>
    <circle cx="62" cy="510" r="128" fill="none" stroke="#f18a1c" stroke-width="5"/>
    <path d="M0 384 Q40 370 78 372" fill="none" stroke="#f18a1c" stroke-width="1.6"/>
  </svg>

  <div class="abs brand-mark"></div>
  <div class="abs brand-name">VANTORA GROUP</div>

  <div class="abs headline">
    <div class="headline__dark">VANTORA GROUP -</div>
    <div class="headline__dark">POWERING</div>
    <div class="headline__accent">Progression with</div>
    <div class="headline__accent">People</div>
  </div>
  <div class="abs services-title">Our<br>Services</div>
  <p class="abs services-intro">We know Accounting &amp; Finance! We realize the knowledge and perseverance it takes to stay ahead in this innovative industry. Vantora Group offers a dynamic scale of services to cater to our clients' ever-changing needs. Whether you need Accounting &amp; Finance resources or you're outsourcing vendor management, Vantora can provide tailored solutions to service your needs.</p>

  <div class="abs service-icon service-icon--tech"><div class="service-icon__art" role="img" aria-label="Illustration of a light bulb with gears"></div></div>
  <div class="abs service-icon service-icon--finance"><div class="service-icon__art" role="img" aria-label="Illustration of coins and money"></div></div>
  <div class="abs service-icon service-icon--health"><div class="service-icon__art" role="img" aria-label="Illustration of medicine capsules and a pill bottle"></div></div>

  <div class="abs service service--tech">
    <h3 class="service__title">TECHNOLOGY</h3>
    <p class="service__text">Vantora Technology provides staffing solutions for companies seeking top talent. We partner with the most sought-after IT professionals to help them achieve their career goals.</p>
  </div>
  <div class="abs service service--finance">
    <h3 class="service__title">ACCOUNTING &amp; FINANCE</h3>
    <p class="service__text">Vantora Group provides staffing solutions for companies seeking top talent. We partner with the most sought-after Accounting and Finance professionals to help them achieve their career goals.</p>
  </div>
  <div class="abs service service--health">
    <h3 class="service__title">HEALTHCARE IT</h3>
    <p class="service__text">Proper use of technology plays a vital role in patient care. Vantora Group assists healthcare providers to optimize the utilization of EMR/EHR systems.</p>
  </div>

  <div class="abs contact-bar contact-bar--front">
    <span class="contact-bar__item">
      <svg class="contact-bar__icon" viewBox="0 0 10 10"><rect width="10" height="10" rx="2" fill="#f18a1c"/><path d="M3 2.5 Q2.3 5.5 6.5 7.6 L7.4 6.6 L6 5.7 L5.4 6.2 Q4.2 5.5 3.9 4.3 L4.4 3.8 L3.6 2.4Z" fill="#1c1c1e"/></svg>
      555.014.2290
    </span>
    <span class="contact-bar__item">
      <svg class="contact-bar__icon" viewBox="0 0 10 10" fill="none" stroke="#f18a1c" stroke-width="0.9"><circle cx="5" cy="5" r="4.3"/><ellipse cx="5" cy="5" rx="1.9" ry="4.3"/><path d="M0.7 5H9.3M1.4 2.8H8.6M1.4 7.2H8.6"/></svg>
      www.vantoragroup.com
    </span>
  </div>
</section>

<!-- BACK -->
<section class="sheet sheet--back" aria-label="Flyer back">
  <svg class="deco" viewBox="0 0 430 607">
    <defs>
      <linearGradient id="meetingTone" x1="0" y1="0" x2="1" y2="1">
        <stop offset="0" stop-color="#4a4e55"/>
        <stop offset="0.45" stop-color="#b9b2a6"/>
        <stop offset="0.75" stop-color="#a98a62"/>
        <stop offset="1" stop-color="#5a4f45"/>
      </linearGradient>
    </defs>
    <g role="img" aria-label="Photo of a team meeting around a conference table">
      <rect x="0" y="0" width="130" height="232" fill="url(#meetingTone)"/>
      <circle cx="130" cy="122" r="138" fill="url(#meetingTone)"/>
    </g>
    <path d="M168 -17 A147 147 0 1 1 68 258" fill="none" stroke="#f18a1c" stroke-width="5" aria-hidden="true"/>
  </svg>

  <h2 class="abs about-title">ABOUT US</h2>
  <div class="abs about-rule"></div>
  <p class="abs about-text about-text--lead">Vantora Group is a nationwide<br>leader of employment<br>solutions. Our ability to build<br>strategic relationships<br>between Accounting and<br>Finance professionals and<br>dynamic organizations make us<br>an invaluable resource to meet-<br>ing business objectives.</p>
  <p class="abs about-text about-text--detail">The Vantora team has over 20 years of<br>industry experience enabling us to<br>tailor business solutions to meet your<br>individual needs. In today's competitive<br>marketplace, there are countless challenges<br>associated with locating and retaining specialty<br>talent. We offer a wide variety of solutions<br>enabling our clients and professionals to seize<br>opportunities within a competitive and progressive<br>industry.</p>

  <h3 class="abs mission-title">MISSION STATEMENT</h3>
  <div class="abs mission-rule"></div>
  <p class="abs mission-text">Since Vantora Group's inception, we have prided ourselves on our ability to establish long-term partnerships, which represent the core of our business. Our mission is to enhance these relationships through our established core values and business practices.</p>

  <div class="abs pledge pledge--customers">
    <div class="pledge__head"><svg class="pledge__chevron" viewBox="0 0 8 9"><path d="M1.5 1 L5.5 4.5 L1.5 8" fill="none" stroke="#f18a1c" stroke-width="1.8"/></svg>TO OUR CUSTOMERS:</div>
    <p class="pledge__text">We consistently provide the highest level of value, service and respect to our customers. Our proven value is driven by professionals committed to providing a superior product. We will stop at nothing to provide the best level of service with organizations that recognize our value and look to establish long-term partnerships.</p>
  </div>
  <div class="abs pledge pledge--consultants">
    <div class="pledge__head"><svg class="pledge__chevron" viewBox="0 0 8 9"><path d="M1.5 1 L5.5 4.5 L1.5 8" fill="none" stroke="#f18a1c" stroke-width="1.8"/></svg>TO OUR CONSULTANTS:</div>
    <p class="pledge__text">We fully commit to provide value for our consultants. Our goal is to provide every job seeker with marketable opportunities and applicable resources that will guide them in achieving their individual business pursuits. Through honest business practices, respect and open communication we strive to counsel our partners in achieving career success.</p>
  </div>
  <div class="abs pledge pledge--employees">
    <div class="pledge__head"><svg class="pledge__chevron" viewBox="0 0 8 9"><path d="M1.5 1 L5.5 4.5 L1.5 8" fill="none" stroke="#f18a1c" stroke-width="1.8"/></svg>TO OUR EMPLOYEES:</div>
    <p class="pledge__text">Employees that reflect our core values are our number one commitment. We have created a working environment that fairly rewards performance, creativity, teamwork and ownership. It is our collective responsibility to challenge and educate one another to achieve personal and shared success.</p>
  </div>

  <div class="abs photo-desk" role="img" aria-label="Photo of laptops showing charts on a shared desk"></div>

  <div class="abs contact-bar contact-bar--back">
    <span class="contact-bar__item">
      <svg class="contact-bar__icon" viewBox="0 0 10 10"><path d="M5 0.6 A3.3 3.3 0 0 1 8.3 3.9 C8.3 6.2 5 9.4 5 9.4 C5 9.4 1.7 6.2 1.7 3.9 A3.3 3.3 0 0 1 5 0.6Z" fill="#f18a1c"/><circle cx="5" cy="3.9" r="1.3" fill="#1c1c1e"/></svg>
      <span class="contact-bar__address">120 Alder Creek Way, Suite 400 Fairview,<br>TN 37000</span>
    </span>
    <span class="contact-bar__item">
      <svg class="contact-bar__icon" viewBox="0 0 10 10"><rect width="10" height="10" rx="2" fill="#f18a1c"/><path d="M3 2.5 Q2.3 5.5 6.5 7.6 L7.4 6.6 L6 5.7 L5.4 6.2 Q4.2 5.5 3.9 4.3 L4.4 3.8 L3.6 2.4Z" fill="#1c1c1e"/></svg>
      555.014.2290
    </span>
    <span class="contact-bar__item">
      <svg class="contact-bar__icon" viewBox="0 0 10 10" fill="none" stroke="#f18a1c" stroke-width="0.9"><circle cx="5" cy="5" r="4.3"/><ellipse cx="5" cy="5" rx="1.9" ry="4.3"/><path d="M0.7 5H9.3M1.4 2.8H8.6M1.4 7.2H8.6"/></svg>
      www.vantoragroup.com
    </span>
  </div>
</section>

</body>
</html>
```